Business Card Design for a Lending Business (Hard Money loans)

We need a business card for our Real Estate Lending business. We do hard Money loans for real estate investors. We have an existing logo we like, see attached. I'd like the business card to mostly include the logo colors, but a bright color pop of some sort would be nice to see also. Card should include Logo, Company Name, Company Address, Employee Name, Cell Phone, Main Phone, Email, Website

Industry/Entity Type

Finance / Lending

Contact Information for Business Card

Logo, Company Name, Company Address, Employee Name, Cell Phone, Main Phone, Email, Website

Requirements
Nice to have
• I'd like the business card to mostly include the logo colors, but a bright color pop of some sort would be nice to see also.

```html
<!DOCTYPE html>
<html lang="en">
<head>
<meta charset="utf-8">
<title>Harbor Ridge Lending – Business Card</title>
<link href="https://fonts.googleapis.com/css2?family=Mulish:wght@400;600;800&display=swap" rel="stylesheet">
<style>
  :root {
    --navy: #273582;
    --sky: #13a9dc;
    --ink: #3b3b45;
    --card: #f6f6f6;
    --backdrop: #e2e2e2;
  }
  * { margin: 0; padding: 0; box-sizing: border-box; }
  html, body { width: 1200px; height: 1200px; overflow: hidden; }
  body {
    background: var(--backdrop);
    font-family: "Mulish", sans-serif;
    color: var(--ink);
    position: relative;
  }
  .card {
    position: absolute;
    left: 235px;
    width: 730px;
    height: 416px;
    background: var(--card);
  }
  .card--front { top: 160px; }
  .card--back { top: 631px; }

  .brand {
    position: absolute;
    display: flex;
    flex-direction: column;
    align-items: center;
  }
  .brand__dot {
    border-radius: 50%;
    background: var(--sky);
  }
  .brand__name {
    font-weight: 800;
    color: var(--navy);
    letter-spacing: 0.06em;
    text-transform: uppercase;
    text-align: center;
    line-height: 1.1;
  }
  .card--front .brand { left: 0; right: 0; top: 118px; }
  .card--front .brand__dot { width: 84px; height: 84px; margin-bottom: 22px; }
  .card--front .brand__name { font-size: 30px; }

  .website {
    position: absolute;
    left: 0; right: 0; top: 346px;
    text-align: center;
    font-size: 19px;
    color: var(--ink);
  }
  .website__domain { color: var(--navy); }

  .card--back .brand { left: 430px; width: 300px; top: 48px; }
  .card--back .brand__dot { width: 64px; height: 64px; margin-bottom: 16px; }
  .card--back .brand__name { font-size: 22px; }

  .person { position: absolute; left: 52px; top: 208px; }
  .person__name { font-size: 31px; font-weight: 800; color: var(--navy); line-height: 1.1; }
  .person__title { font-size: 18px; margin-top: 8px; }

  .contact-list {
    position: absolute; left: 52px; top: 290px;
    list-style: none;
  }
  .contact-list li {
    display: flex; align-items: center;
    font-size: 19px; height: 26px;
  }
  .contact-list svg { width: 16px; height: 16px; margin-right: 10px; fill: var(--navy); }

  .address {
    position: absolute; right: 53px; top: 316px;
    text-align: right; font-size: 19px; line-height: 28px;
    font-style: normal;
  }
</style>
</head>
<body>
  <section class="card card--front">
    <div class="brand">
      <span class="brand__dot"></span>
      <span class="brand__name">Harbor Ridge Lending</span>
    </div>
    <p class="website">www.<span class="website__domain">harborridgelending</span>.com</p>
  </section>

  <section class="card card--back">
    <div class="brand">
      <span class="brand__dot"></span>
      <span class="brand__name">Harbor Ridge Lending</span>
    </div>

    <div class="person">
      <h1 class="person__name">Marcus Delaney</h1>
      <p class="person__title">Founder &amp; Director</p>
    </div>

    <ul class="contact-list">
      <li>
        <svg viewBox="0 0 16 16" aria-hidden="true"><path d="M3.6 1.2l2.3 2.6-1.4 1.8c.9 2 2.4 3.6 4.4 4.6l1.8-1.4 2.6 2.3-1.4 2.5C6.6 13.4 2.6 9.4 1.3 2.6z"/></svg>
        410-555-0142
      </li>
      <li>
        <svg viewBox="0 0 16 16" aria-hidden="true"><path d="M4 1h8v4H4zM1 6h14v6h-3v3H4v-3H1zm4 4v4h6v-4z"/></svg>
        410-555-0187
      </li>
      <li>
        <svg viewBox="0 0 16 16" aria-hidden="true"><path d="M1 3h14v10H1zm1.5 1.5L8 8.5l5.5-4z"/></svg>
        info@HarborRidgeLending.com
      </li>
    </ul>

    <address class="address">
      2150 Linden Mill Rd.<br>
      Fallston MD 21047
    </address>
  </section>
</body>
</html>
```